High-end water purification system

8 or 12-page brochure for our Water Purification System

We are a new company who manufactures a very high-end unpowered water purification system, which generates hydrogen, negative ions, small molecular clustered, alkaline and natural minerals in water. We want a professional booklet on our launching product with a brief of the company. Make sure to fully understand our product for a better understanding and clearer image.

Size: standard (us letter, magazine size)

Font: No preference, logo is in sansation

Color: No preference, could use logo color

Target Market(s)

Parents, female, healthy wealthy people

Industry/Entity Type

Health And Wellness

Font styles to use
Serif

Colors

Designer to choose colors to be used in the design.

Requirements
Must have
• Look up and use pictures/graphics that give customer a visual look and better understanding
• Create a safe and trustworthy image
• Make the content flow naturally, make sense to the readers
• Easy to read
• Good balance of white space
Nice to have
• Make infographics :
• 1. water related diseases
• 2. the population rate for chronic diseases
• 3. system description, including stages of filter/generators
• 4. the 5 main Features
Should not have
• Too much words crowded in one page

```html
<!DOCTYPE html>
<html lang="en">
<head>
<meta charset="utf-8">
<title>Aquavelle Brochure Spreads</title>
<link href="https://fonts.googleapis.com/css2?family=Exo+2:wght@300;700&family=Open+Sans:wght@400;600;700&display=swap" rel="stylesheet">
<style>
  :root{
    --stage-light:#9a9a9a;
    --stage-dark:#6c6c6c;
    --navy:#1b2170;
    --blue:#2d3da3;
    --sky:#46b2e6;
    --sky-light:#bfe6f8;
    --ink:#4a4a4a;
    --paper:#ffffff;
    --faint:#f0f1f4;
    --icon:#8e939c;
    --cover-bg:#1c1c1c;
  }
  *{margin:0;padding:0;box-sizing:border-box}
  html,body{width:1018px;height:1200px;overflow:hidden}
  body{
    position:relative;
    background:radial-gradient(ellipse at 50% 50%,var(--stage-light) 0%,var(--stage-dark) 100%);
    font-family:"Open Sans",Arial,sans-serif;
    color:var(--ink);
  }
  .page{position:absolute;width:419px;height:542px;background:var(--paper);overflow:hidden;box-shadow:0 2px 6px rgba(0,0,0,.25)}
  .page--cover{left:50px;top:42px;background:linear-gradient(180deg,#262626 0%,var(--cover-bg) 60%,#121212 100%)}
  .page--one{left:526px;top:42px}
  .page--two{left:50px;top:614px}
  .page--three{left:526px;top:614px}

  .page-label{position:absolute;color:#f2f2f2;font-size:20px;font-weight:400;transform:rotate(-90deg);transform-origin:left bottom;white-space:nowrap;letter-spacing:.5px}

  /* cover */
  .cover-brand{position:absolute;top:48px;left:0;width:100%;text-align:center;font-weight:600;font-size:40px;color:#fff;letter-spacing:2px}
  .cover-photo{
    position:absolute;left:0;top:150px;width:419px;height:250px;
    background:
      radial-gradient(ellipse 34% 46% at 50% 48%,rgba(210,214,218,.55) 0%,rgba(120,124,128,.35) 55%,rgba(40,40,40,0) 100%),
      radial-gradient(ellipse 60% 40% at 50% 55%,rgba(90,92,95,.45) 0%,rgba(28,28,28,0) 100%);
  }
  .cover-tagline{position:absolute;left:0;width:100%;text-align:center;font-family:"Exo 2",sans-serif;color:#f4f4f4}
  .cover-tagline--light{top:424px;font-weight:300;font-size:25px;letter-spacing:1.5px}
  .cover-tagline--bold{top:454px;font-weight:700;font-size:36px;letter-spacing:1.5px;color:#e2e2e2}
  .cover-reflection{position:absolute;left:0;bottom:0;width:100%;height:50px;background:linear-gradient(180deg,rgba(60,60,60,0),rgba(90,90,90,.3))}

  /* shared inner page */
  .tag{position:absolute;left:0;top:25px;height:11px;width:138px;background:var(--navy);clip-path:polygon(0 0,100% 0,93% 100%,0 100%);color:#fff;font-size:6.5px;font-weight:600;line-height:11px;padding-left:25px}
  .brand{position:absolute;right:24px;top:24px;font-weight:600;font-size:12.5px;color:var(--navy);letter-spacing:.5px}
  .watermark{position:absolute;left:10px;top:462px;transform:rotate(-90deg);transform-origin:left top;font-weight:700;font-size:70px;color:var(--faint);letter-spacing:6px;white-space:nowrap}
  .heading{position:absolute;font-weight:700;font-size:18px;color:var(--navy);border-left:2px solid var(--navy);padding-left:8px;line-height:17px}
  .heading .accent{color:var(--blue)}
  .body-copy{position:absolute;font-size:7.1px;line-height:11.6px;color:var(--ink);text-align:justify}
  .folio{position:absolute;left:0;top:506px;width:100%;height:12px}
  .folio::before{content:"";position:absolute;left:0;right:0;top:6px;border-top:1px solid #c9ccd6}
  .folio span{position:absolute;left:50%;top:0;width:12px;height:12px;margin-left:-6px;border-radius:50%;background:#fff;border:1px solid var(--navy);font-size:7px;line-height:10px;text-align:center;color:var(--navy);font-weight:600}

  /* page one */
  .mission-lines{position:absolute;left:46px;top:232px;font-size:7.8px;line-height:13px;font-weight:600;color:var(--blue)}
  .photo-dancer{
    position:absolute;left:200px;top:180px;width:219px;height:330px;
    background:radial-gradient(ellipse 45% 50% at 55% 55%,rgba(120,175,215,.55) 0%,rgba(170,210,235,.35) 45%,rgba(255,255,255,0) 100%);
  }
  .photo-sea{position:absolute;left:0;bottom:0;width:419px;height:140px;background:linear-gradient(180deg,rgba(255,255,255,0) 0%,rgba(170,200,225,.6) 40%,#5b87b3 75%,#23466f 100%)}

  /* page two */
  .value-icon{position:absolute;width:20px;height:20px}
  .value-title{position:absolute;width:150px;text-align:center;font-weight:700;font-size:12.5px;color:var(--blue)}
  .photo-glass{
    position:absolute;left:200px;top:0;width:219px;height:542px;
    background:
      linear-gradient(90deg,rgba(255,255,255,1) 0%,rgba(255,255,255,0) 30%),
      linear-gradient(180deg,rgba(255,255,255,0) 0%,rgba(255,255,255,0) 50%,rgba(200,204,208,.55) 70%,rgba(150,154,158,.6) 88%,rgba(235,236,238,.8) 100%);
  }

  /* page three */
  .quote{position:absolute;left:50px;width:320px;text-align:center;font-size:7.6px;line-height:11px;color:var(--blue);font-weight:400}
  .quote b{color:#a8acb4;font-weight:700;font-size:10px}
  .quote-source{position:absolute;right:63px;top:80px;font-size:7px;color:#333}
  .faucet{position:absolute;left:200px;top:132px;width:54px;height:62px;background:radial-gradient(ellipse 50% 50% at 50% 50%,#c7cacd 0%,#e6e7e8 60%,rgba(255,255,255,0) 100%)}
  .drop-title{position:absolute;left:150px;top:248px;width:120px;text-align:center;font-weight:700;font-size:15px;line-height:17px;color:#fff}
  .drop-text{position:absolute;left:152px;top:298px;width:116px;text-align:center;font-size:5.6px;line-height:9px;color:#1c2a55}
  .disease{position:absolute;font-size:7.4px;line-height:9px;font-weight:600;color:var(--blue);text-align:center}
  .disease-list{position:absolute;left:85px;top:222px;font-size:5.6px;line-height:9.3px;color:#333;list-style:none}
  .disease-list li::before{content:"▸ ";color:var(--sky)}
  .stats{position:absolute;left:57px;top:427px;width:320px;font-size:6.3px;line-height:10.6px;color:#333}
  .closing{position:absolute;left:40px;top:482px;width:340px;text-align:center;font-size:7.4px;line-height:10.6px;font-weight:700;color:var(--sky)}
</style>
</head>
<body>

  <!-- Cover -->
  <section class="page page--cover">
    <div class="cover-brand">AQUAVELLE</div>
    <div class="cover-photo" role="img" aria-label="White countertop water purifier with water splashing around it on a dark background"></div>
    <div class="cover-tagline cover-tagline--light">LEADING THE WATER</div>
    <div class="cover-tagline cover-tagline--bold">REVOLUTION</div>
    <div class="cover-reflection"></div>
  </section>
  <div class="page-label" style="left:500px;top:560px">cover</div>

  <!-- Page 1 -->
  <section class="page page--one">
    <div class="watermark">AQUAVELLE</div>
    <div class="photo-sea" role="img" aria-label="Calm blue water surface with splashes"></div>
    <div class="photo-dancer" role="img" aria-label="Ballerina in a white tutu rising from a swirl of splashing water"></div>
    <div class="tag">Leading The Water Revolution</div>
    <div class="brand">AQUAVELLE</div>

    <h2 class="heading" style="left:46px;top:58px">Philosophy</h2>
    <p class="body-copy" style="left:46px;top:87px;width:328px">Our body is composed of 60-75% of water; our blood is composed of 92% of water. Water is in fact an extremely crucial factor to maintain body's health. We believe that the most effective and direct way to retain and improve one's health condition is by changing the water one drink every day. Good quality water possesses the qualities as those found in natural springs in environment-preserved areas: clean as in without impurities, high alkaline level, hydrogen rich, high level of negative ions, and small molecular clustered. Aquavelle urge to raise more awareness on the quality of daily drinking water and their effect on our overall and cellular health. We advocate the most natural way to maintain and regain body's health.</p>

    <h2 class="heading" style="left:46px;top:206px">Mission</h2>
    <div class="mission-lines">To bring health, beauty, and happiness<br>To diminish world's chronic diseases<br>To create value and make a difference</div>
    <p class="body-copy" style="left:46px;top:280px;width:170px;font-size:7.4px;line-height:13px">We consider our mission statement a commitment to our customers. We deliver on that commitment by striving to create and provide the best drinking water that most benefit human body</p>

    <div class="folio"><span>1</span></div>
  </section>
  <div class="page-label" style="left:976px;top:560px">Page 1</div>

  <!-- Page 2 -->
  <section class="page page--two">
    <div class="watermark">AQUAVELLE</div>
    <div class="photo-glass" role="img" aria-label="Stream of water pouring into a clear drinking glass"></div>
    <div class="tag">Leading The Water Revolution</div>
    <div class="brand">AQUAVELLE</div>

    <h2 class="heading" style="left:45px;top:60px">Vision</h2>
    <p class="body-copy" style="left:46px;top:87px;width:229px">Have Aquavelle Water Purification System in every kitchen, ending the fear and suffer of major chronic diseases and becoming the quality leader in water purification industry.</p>

    <h2 class="heading" style="left:45px;top:137px">Core <span class="accent">Values</span></h2>

    <svg class="value-icon" style="left:118px;top:184px" viewBox="0 0 20 20" aria-hidden="true"><g fill="none" stroke="var(--icon)" stroke-width="1.6" stroke-linecap="round"><path d="M6 17 L4 10 M8 17 L7 5 M10 17 L10 3 M12 17 L13 5 M14 17 L16 9"/></g></svg>
    <div class="value-title" style="left:55px;top:206px">Our Faith</div>
    <p class="body-copy" style="left:55px;top:227px;width:150px">Aquavelle is confident in solving many of your health concerns. With a three-month risk-free improvement guarantee, customers with diabetes type II, high blood pressure, high cholesterol, and high triglyceride are assured to get the results they are looking for and to be completely satisfy with the experience. Our customers value highly in their health, and we care deeply for our customers.</p>

    <svg class="value-icon" style="left:120px;top:363px" viewBox="0 0 20 20" aria-hidden="true"><g fill="none" stroke="var(--icon)" stroke-width="1.6" stroke-linecap="round" stroke-linejoin="round"><path d="M1 8 L5 6 L9 8 L13 6 L19 9"/><path d="M5 10 L9 14 L11 13 L13 14 L16 11"/></g></svg>
    <div class="value-title" style="left:55px;top:385px">Our Responsibility</div>
    <p class="body-copy" style="left:55px;top:405px;width:150px">Aquavelle cares deeply for our customer as well as our environment. Aquavelle insist on saving energy resources while protecting the environment. The whole system is smart designed but unpowered, does not discharge waste water, and protects you from radiation or EMF emissions.</p>

    <div class="folio"><span>2</span></div>
  </section>
  <div class="page-label" style="left:500px;top:1132px">Page 2</div>

  <!-- Page 3 -->
  <section class="page page--three">
    <div class="tag">Leading The Water Revolution</div>
    <div class="brand">AQUAVELLE</div>

    <p class="quote" style="top:54px"><b>“</b> Water and Sanitation is one of the primary drivers of public health. I often refer to it as “Health 101”... <b>”</b></p>
    <div class="quote-source">– Global Water Health Council</div>
    <p class="quote" style="top:98px"><b>“</b> Water-Related Diseases are responsible for 80 percent of all illnesses, deaths...” <b>”</b></p>

    <div class="faucet" role="img" aria-label="Chrome water tap"></div>

    <svg style="position:absolute;left:0;top:0" width="419" height="542" viewBox="0 0 419 542" aria-hidden="true">
      <defs>
        <linearGradient id="dropFill" x1="0" y1="0" x2="0" y2="1">
          <stop offset="0" stop-color="#8ad6f5"/>
          <stop offset="1" stop-color="#46b2e6"/>
        </linearGradient>
      </defs>
      <path d="M210 198 C228 232 282 270 282 318 C282 356 250 380 210 380 C170 380 138 356 138 318 C138 270 192 232 210 198 Z" fill="url(#dropFill)" stroke="#bfe6f8" stroke-width="4"/>
      <g fill="none" stroke="#6d86c8" stroke-width=".7">
        <polyline points="180,210 173,210"/>
        <polyline points="162,250 162,265 166,265"/>
        <polyline points="120,315 140,315"/>
        <polyline points="125,362 132,362 132,350 145,350"/>
        <polyline points="168,404 172,404 172,376"/>
        <polyline points="240,406 240,376"/>
        <polyline points="290,378 290,360 280,360"/>
        <polyline points="296,322 284,322"/>
        <polyline points="276,258 276,265 310,265"/>
      </g>
      <g fill="#fff" stroke="#b4b8c0" stroke-width=".8">
        <circle cx="121" cy="191" r="10"/>
        <circle cx="99" cy="286" r="10"/>
        <circle cx="99" cy="340" r="10"/>
        <circle cx="144" cy="386" r="10"/>
        <circle cx="222" cy="391" r="10"/>
        <circle cx="318" cy="355" r="10"/>
        <circle cx="326" cy="288" r="10"/>
        <circle cx="310" cy="232" r="10"/>
      </g>
      <g fill="none" stroke="#6e737c" stroke-width="1" stroke-linecap="round" stroke-linejoin="round">
        <!-- heart -->
        <path d="M121 197 L115.5 191.5 A3 3 0 0 1 121 187.5 A3 3 0 0 1 126.5 191.5 Z"/>
        <!-- kidneys -->
        <path d="M96 281 C92 281 92 291 96 291 C98 291 98 288 97 286 C98 284 98 281 96 281 Z"/>
        <path d="M102 281 C106 281 106 291 102 291 C100 291 100 288 101 286 C100 284 100 281 102 281 Z"/>
        <!-- liver -->
        <path d="M93 337 C97 334 106 334 105 338 C104 342 98 345 95 344 C93 343 92 339 93 337 Z"/>
        <!-- ribbon -->
        <path d="M141 393 L146 382 A2.5 2.5 0 1 0 142 382 L147 393"/>
        <!-- brain -->
        <path d="M216 393 C214 389 217 386 220 387 C221 384 225 384 226 387 C229 387 230 391 228 393 C226 395 218 395 216 393 Z M222 387 L222 394"/>
        <!-- nerve -->
        <path d="M314 361 C314 355 322 355 322 350 M318 357 L322 359 M316 353 L313 350"/>
        <!-- immune / helix -->
        <path d="M322 282 C330 286 322 290 330 294 M330 282 C322 286 330 290 322 294"/>
        <!-- infection -->
        <circle cx="310" cy="232" r="3.5"/>
        <path d="M310 225 L310 227 M310 237 L310 239 M303 232 L305 232 M315 232 L317 232 M305 227 L306.5 228.5 M313.5 235.5 L315 237 M315 227 L313.5 228.5 M306.5 235.5 L305 237"/>
      </g>
    </svg>

    <div class="drop-title">WATER<br>RELATED<br>DISEASE</div>
    <div class="drop-text">Caused by drinking untreated water, tap water, distilled water, bottled water and water with impurities including toxic chemicals, heavy metals, fluoride, lead, chlorine, radiological hazards, infectious agents</div>

    <div class="disease" style="left:73px;top:206px">Cardiovascular Disease</div>
    <ul class="disease-list">
      <li>Diabetes Type II</li>
      <li>High Blood Pressure</li>
      <li>High Cholesterol</li>
      <li>High Triglyceride</li>
      <li>High Uric Acid</li>
    </ul>
    <div class="disease" style="left:64px;top:302px">Chronic Kidney<br>Disease</div>
    <div class="disease" style="left:67px;top:354px">Chronic Liver<br>Disease</div>
    <div class="disease" style="left:130px;top:401px">Cancer</div>
    <div class="disease" style="left:198px;top:403px">Brain Damage</div>
    <div class="disease" style="left:278px;top:369px">Autonomous Nervous<br>System Disorder</div>
    <div class="disease" style="left:294px;top:302px">Immune System<br>Disorder</div>
    <div class="disease" style="left:291px;top:244px">Infectious<br>Diseases</div>

    <p class="stats">29 % of population have high blood pressure, greatly increases the risk for heart disease and stroke, the first and third leading causes of death in the United States as in 2016<br>15 % of population have chronic kidney disease, which leads to hemodialysis<br>9.3 % of population have Diabetes, and 1/3 of the population has been diagnosed as pre-diabetes</p>
    <p class="closing">DRINKING WATER WITH IMPURITIES WILL SLOWLY CAUSE SEVERE DAMAGE TO HUMAN BRAIN AND BODY</p>

    <div class="folio"><span>3</span></div>
  </section>
  <div class="page-label" style="left:976px;top:1132px">Page 3</div>

</body>
</html>
```